Etiketten-Design für Weinflasche
Helga hat mit sehr viel Mühe und Hingabe unsere Wünsche umgesetzt. Wir sind mit dem Endergebnis sehr zufrieden.
Zielgruppe
Wir sind ein Weingut-Startup und suchen ein frisches, hochwertiges Design für unsere Flaschenetiketten.
Aufgabenstellung
Wir benötigen ein Vorderetikett für unsere Weinflaschen mit folgenden Vorgaben:
- Etiketten sollen variabel nutzbar sein, für verschiedene Rebsorten bspw. in versch. Farben
- Auf dem Etikett zwingend: Logo (siehe Anlage), Rebsorte, Anbaugebiet (Nahe)
- Wiedererkennungswert
- nicht zu klassisch, nicht zu futuristisch (gutes Mittelmaß, wie beim Logo auch)
- ggf. Spiel mit (Hintergrund-)Farben für verschiedene Sorten, ggf. Hintergrundmuster (evtl. Höhenlinien des Talwiesers, Bad Kreuznach (unser Heimatberg))
- Anpassung an verschiedene Qualitätsstufen (Gutswein, Ortswein, Lagenwein), ggf. schwarzes Sonderetikett für absolutes Premiumsegment
- unsere Werte als Naturnah und familiengeführtes Weingut sollen transportiert werden
- Maß: 80x90mm (breitxhoch)
Insgesamt sind wir offen für verschiedene Vorschläge, auch wenn die Vorgaben oben teils sehr konkret sind. Bei guten Designs lassen wir uns gerne von unseren Vorstellungen abbringen ;)

```html
<!DOCTYPE html>
<html lang="de">
<head>
<meta charset="utf-8">
<title>Weingut Lenz – Etikettenserie</title>
<link rel="stylesheet" href="https://fonts.googleapis.com/css2?family=Ubuntu:ital,wght@0,300;0,400;1,300&display=swap">
<style>
  :root {
    --ink: #1c1c1c;
    --band-dark: #2a2a2a;
    --band-light: #4a4a4a;
    --paper-1: #fbfbc8;
    --paper-2: #ffffe6;
    --cream: #efe4c8;
    --muted: #6a6a6a;
    --stripe-grey: #dcdcdc;
    --stripe-rose: #e9c6c8;
    --stripe-mint: #d3f2d8;
    --stripe-sand: #ede2c6;
    --swatch-aqua: #c9f3f0;
    --swatch-green: #d6f0d0;
    --swatch-seafoam: #cdf0e0;
    --vine-light: #efefc4;
    --vine-dark: #333333;
    --canvas: #ffffff;
  }
  * { box-sizing: border-box; margin: 0; padding: 0; }
  html, body { width: 798px; height: 1200px; overflow: hidden; background: var(--canvas); }
  body { position: relative; font-family: "Ubuntu", sans-serif; color: var(--ink); }

  /* Label: built at 252 × 316 units, bottle versions scaled down */
  .label {
    position: absolute;
    width: 252px;
    height: 316px;
    overflow: hidden;
    background: linear-gradient(90deg, var(--paper-1), var(--paper-2) 70%, var(--paper-1));
    --stripe: var(--stripe-grey);
    --text: var(--ink);
    --vine: var(--vine-light);
    --origin: var(--muted);
  }
  .label--feature { left: 137px; top: 45px; }
  .label--bottle { top: 745px; transform: scale(0.663); transform-origin: 0 0; }
  .label--cabernet { left: 72px; --stripe: var(--stripe-rose); }
  .label--riesling { left: 319px; --stripe: var(--stripe-mint); }
  .label--cuvee {
    left: 561px;
    --stripe: var(--stripe-sand);
    --text: var(--cream);
    --vine: var(--vine-dark);
    --origin: #9a9a9a;
    background: linear-gradient(135deg, var(--band-light), var(--band-dark));
  }

  .label__band {
    position: absolute; left: 0; top: 0; width: 100%; height: 76px;
    background: linear-gradient(100deg, var(--band-dark) 30%, var(--band-light) 65%, var(--band-dark));
  }
  .label__stripe {
    position: absolute; left: 0; top: 76px; width: 100%; height: 12px;
    background: var(--stripe);
  }
  .label__brand {
    position: absolute; left: 22px; top: 38px;
    font-weight: 300; font-size: 30px; line-height: 1;
    color: #ffffff;
  }
  .label__vine {
    position: absolute; left: 6px; top: 92px; width: 156px; height: 52px;
  }
  .label--cuvee .label__vine { width: 112px; }

  .label__variety {
    position: absolute; left: 124px; top: 150px;
    font-weight: 300; font-size: 30px; line-height: 28px;
    color: var(--text);
  }
  .label--cabernet .label__variety { top: 158px; font-size: 26px; line-height: 25px; }
  .label--riesling .label__variety { top: 152px; font-size: 40px; line-height: 36px; }
  .label--cuvee .label__variety { top: 111px; font-size: 26px; line-height: 25px; }

  .label__origin {
    position: absolute; left: 82px; top: 274px;
    font-style: italic; font-weight: 300; font-size: 9px; line-height: 1;
    color: var(--origin);
  }
  .label__vintage {
    position: absolute; left: 124px; top: 286px;
    font-weight: 400; font-size: 10px; line-height: 1;
    color: var(--text);
  }

  .palette { position: absolute; left: 604px; top: 95px; width: 99px; }
  .palette__swatch { height: 15px; }
  .palette__swatch--aqua { background: var(--swatch-aqua); }
  .palette__swatch--green { background: var(--swatch-green); }
  .palette__swatch--grey { background: var(--stripe-grey); }
  .palette__swatch--rose { background: var(--stripe-rose); }
  .palette__swatch--sand { background: var(--stripe-sand); }
  .palette__swatch--seafoam { background: var(--swatch-seafoam); }

  .brand-mark {
    position: absolute; left: 604px; top: 1140px;
    font-weight: 300; font-size: 32px; line-height: 1;
    color: var(--ink);
  }
</style>
</head>
<body>

  <section class="label label--feature">
    <div class="label__band"></div>
    <div class="label__stripe"></div>
    <span class="label__brand">lenz</span>
    <svg class="label__vine" role="img" aria-label="Rankenornament mit Weinblatt" viewBox="0 0 100 40" preserveAspectRatio="none">
      <rect width="100" height="40" rx="4" fill="var(--vine)"/>
    </svg>
    <h2 class="label__variety">GRAU<br>BUR<br>GUN<br>DER</h2>
    <p class="label__origin">Talwieser Nahe</p>
    <p class="label__vintage">2024</p>
  </section>

  <div class="palette" aria-hidden="true">
    <div class="palette__swatch palette__swatch--aqua"></div>
    <div class="palette__swatch palette__swatch--green"></div>
    <div class="palette__swatch palette__swatch--grey"></div>
    <div class="palette__swatch palette__swatch--rose"></div>
    <div class="palette__swatch palette__swatch--sand"></div>
    <div class="palette__swatch palette__swatch--seafoam"></div>
  </div>

  <section class="label label--bottle label--cabernet">
    <div class="label__band"></div>
    <div class="label__stripe"></div>
    <span class="label__brand">lenz</span>
    <svg class="label__vine" role="img" aria-label="Rankenornament mit Weinblatt" viewBox="0 0 100 40" preserveAspectRatio="none">
      <rect width="100" height="40" rx="4" fill="var(--vine)"/>
    </svg>
    <h2 class="label__variety">CABER<br>NET<br>SAUVIG<br>NON</h2>
    <p class="label__origin">Talwieser Nahe</p>
    <p class="label__vintage">2024</p>
  </section>

  <section class="label label--bottle label--riesling">
    <div class="label__band"></div>
    <div class="label__stripe"></div>
    <span class="label__brand">lenz</span>
    <svg class="label__vine" role="img" aria-label="Rankenornament mit Weinblatt" viewBox="0 0 100 40" preserveAspectRatio="none">
      <rect width="100" height="40" rx="4" fill="var(--vine)"/>
    </svg>
    <h2 class="label__variety">RIES<br>LIN<br>G</h2>
    <p class="label__origin">Talwieser Nahe</p>
    <p class="label__vintage">2024</p>
  </section>

  <section class="label label--bottle label--cuvee">
    <div class="label__band"></div>
    <div class="label__stripe"></div>
    <span class="label__brand">lenz</span>
    <svg class="label__vine" role="img" aria-label="Rankenornament mit Weinblatt" viewBox="0 0 100 40" preserveAspectRatio="none">
      <rect width="100" height="40" rx="4" fill="var(--vine)"/>
    </svg>
    <h2 class="label__variety">CU<br>VEÉ<br>SUPE<br>RIO<br>R</h2>
    <p class="label__origin">Talwieser Nahe</p>
    <p class="label__vintage">2024</p>
  </section>

  <span class="brand-mark">lenz</span>

</body>
</html>
```